New Business Card Design Project

hello again,
i have an awful year and we were not able to complete our logo plan. we would like to use our #1 logo for business card design process. the primary colors for business card should be white background with orange & black letters. our business is mobil truck cranes. we deliver heavy stuff and unload cargo with crane that is mounted on our trucks.
here is our business card info:
HARBOR LIFT HAULERS, INC.
428 WESTCOTT AVE
MERRICK, NY 11542
OFFICE - 516 487 3091
DIRECT - 1 888 LIFT HAULS
MARK@HLHAULERS.COM
PLEASE also try to get our slogan on card .... "Our Loads Keep Rollin"
lastly please also put "24 hour Knuckleboom Service"
you can call me anytime 24/7 to discuss...my cell # is: 516 759 2036
please also list: Mark Delroy, President
Target Market(s)
Heavy Construction industry
Industry/Entity Type
heavy construction industry
Contact Information for Business Card
24 Hr Knuckleboom Service

```html
<!DOCTYPE html>
<html lang="en">
<head>
<meta charset="utf-8">
<title>Harbor Lift Haulers – Business Card</title>
<link href="https://fonts.googleapis.com/css2?family=Montserrat:wght@400;500;700;800&display=swap" rel="stylesheet">
<style>
  :root{
    --orange:#e8812b;
    --black:#111111;
    --paper:#ffffff;
    --ink:#1c1c1c;
    --backdrop:#e9e8e6;
  }
  *{margin:0;padding:0;box-sizing:border-box}
  html,body{width:1200px;height:801px;overflow:hidden}
  body{background:var(--backdrop);font-family:'Montserrat',sans-serif;color:var(--ink);position:relative}
  .card{position:absolute;width:560px;height:320px;background:var(--paper);box-shadow:0 6px 18px rgba(0,0,0,.12)}
  .card--front{left:25px;top:240px}
  .card--back{left:615px;top:240px;display:flex;align-items:center;justify-content:center}

  .brand{position:absolute;left:32px;top:40px;display:flex;align-items:center;gap:12px}
  .brand__dot{width:26px;height:26px;border-radius:50%;background:var(--orange);flex:none}
  .brand__name{font-weight:800;font-size:19px;line-height:1.15;color:var(--black);letter-spacing:.3px}

  .person{position:absolute;left:32px;top:138px}
  .person__name{font-weight:700;font-size:21px;color:var(--orange);letter-spacing:.5px}
  .person__title{font-size:13px;margin-top:2px}
  .address{position:absolute;left:32px;top:200px;font-size:13px;line-height:1.45;letter-spacing:.6px}

  .contacts{position:absolute;left:300px;top:96px;list-style:none}
  .contacts li{display:flex;align-items:center;gap:9px;font-size:13px;letter-spacing:.6px;margin-bottom:9px}
  .contacts svg{width:16px;height:16px;flex:none}

  .band{position:absolute;left:0;right:0;top:270px;height:30px;display:flex}
  .band__slogan{width:42%;background:var(--black);color:#fff;font-size:11.5px;letter-spacing:1px;display:flex;align-items:center;justify-content:center}
  .band__service{flex:1;background:var(--orange);color:#fff;font-size:11.5px;letter-spacing:1px;display:flex;align-items:center;padding-left:22px}

  .back-brand{display:flex;align-items:center;gap:18px}
  .back-brand__dot{width:46px;height:46px;border-radius:50%;background:var(--orange)}
  .back-brand__name{font-weight:800;font-size:32px;line-height:1.12;color:var(--black);letter-spacing:.5px}
</style>
</head>
<body>
  <section class="card card--front">
    <div class="brand">
      <span class="brand__dot"></span>
      <span class="brand__name">HARBOR LIFT<br>HAULERS, INC.</span>
    </div>
    <div class="person">
      <p class="person__name">MARK DELROY</p>
      <p class="person__title">President</p>
    </div>
    <p class="address">428 WESTCOTT AVE<br>MERRICK, NY 11542</p>
    <ul class="contacts">
      <li>
        <svg viewBox="0 0 16 16"><circle cx="8" cy="8" r="8" fill="var(--orange)"/><path d="M5 4.5l1.6-.4 1 2-1 .8c.5 1 1.2 1.8 2.2 2.3l.8-1 2 1-.4 1.6c-3.2.2-6.3-2.9-6.2-6.3z" fill="#fff"/></svg>
        516 487 3091
      </li>
      <li>
        <svg viewBox="0 0 16 16"><circle cx="8" cy="8" r="8" fill="var(--orange)"/><rect x="4" y="5.2" width="8" height="5.6" fill="none" stroke="#fff" stroke-width="1"/><path d="M4 5.4l4 3 4-3" fill="none" stroke="#fff" stroke-width="1"/></svg>
        1 888 LIFT HAULS
      </li>
      <li>
        <svg viewBox="0 0 16 16"><circle cx="8" cy="8" r="8" fill="var(--orange)"/><circle cx="8" cy="8" r="3.8" fill="none" stroke="#fff" stroke-width="1"/><path d="M4.2 8h7.6M8 4.2c-1.8 2.4-1.8 5.2 0 7.6M8 4.2c1.8 2.4 1.8 5.2 0 7.6" fill="none" stroke="#fff" stroke-width=".8"/></svg>
        MARK@HLHAULERS.COM
      </li>
    </ul>
    <div class="band">
      <span class="band__slogan">OUR LOADS KEEP ROLLIN</span>
      <span class="band__service">24 HOUR KNUCKLEBOOM SERVICE</span>
    </div>
  </section>

  <section class="card card--back">
    <div class="back-brand">
      <span class="back-brand__dot"></span>
      <span class="back-brand__name">HARBOR LIFT<br>HAULERS, INC.</span>
    </div>
  </section>
</body>
</html>
```